UK landscaping company needs website

We, Brindle Landscapes need a website design for a company based in Surrey, UK. The design should be bold and playful. We have three main areas of work driveways, paving and fencing. It shouldn't be too heavy in text and concentrate on the pictures from previous jobs we've completed. You may use stock images for the design, these can be changed if you are successful. Please don’t just copy the flyer it is just there to provide content.
We have a logo design which we would also like editing slightly.
Here are some of my local competitors
https://www.vexmoorlandscapes.co.uk/

https://www.twinreedgardendesign.com/

https://quarnelllandscapes.co.uk/

Industry/Entity Type

Landscaping

Coding

Coded - Design and coding required

Number of Pages Required

3 page

Font styles to use
Sans Serif

Requirements
Must have
• Pictures of my previous jobs.
Must be mobile friendly
Easy to navigate
Nice to have
• Try to use different colours. It would be good to have some designs that aren’t just black and green.
I’d like some curves in the design.
Should not have
• We install hard landscaping. Think more building/construction and less plants and cutting grass.

```html
<!DOCTYPE html>
<html lang="en">
<head>
<meta charset="utf-8">
<title>Brindle Landscapes – About</title>
<link rel="stylesheet" href="https://fonts.googleapis.com/css2?family=Roboto:wght@500;700;900&family=Rubik:wght@400;500&display=swap">
<style>
  :root {
    --ink: #231f20;
    --charcoal: #2b2b2b;
    --green: #5cb82e;
    --green-dark: #3f8f1f;
    --grey-band: #ebebeb;
    --text: #3a3a3a;
    --white: #ffffff;
    --head-font: "Roboto", Arial, sans-serif;
    --body-font: "Rubik", Arial, sans-serif;
  }
  * { box-sizing: border-box; margin: 0; padding: 0; }
  html, body { width: 1200px; height: 3041px; overflow: hidden; }
  body { position: relative; background: var(--white); font-family: var(--body-font); color: var(--text); }
  a { color: inherit; }

  .site-header { position: absolute; top: 0; left: 0; width: 1200px; height: 71px; background: var(--ink); z-index: 5; }
  .brand { position: absolute; display: flex; flex-direction: column; color: var(--white); font-family: var(--head-font); font-weight: 700; line-height: 1; text-decoration: none; }
  .brand-main { letter-spacing: -1px; }
  .site-header .brand { left: 130px; top: 10px; }
  .site-header .brand-main { font-size: 37px; }
  .site-header .brand-sub { font-size: 9px; letter-spacing: 1px; margin: 2px 0 0 40px; }
  .main-nav { position: absolute; top: 26px; left: 475px; display: flex; gap: 43px; }
  .main-nav a { font-family: var(--head-font); font-weight: 500; font-size: 17px; color: var(--white); text-decoration: none; letter-spacing: -0.3px; }
  .main-nav a.is-current { color: var(--green); text-decoration: underline; text-underline-offset: 3px; }
  .estimate-box { position: absolute; right: 0; top: 0; width: 201px; height: 71px; background: var(--green); color: var(--white); padding: 13px 0 0 28px; font-family: var(--head-font); }
  .estimate-label { font-size: 15px; font-weight: 500; display: block; }
  .estimate-phone { font-size: 23px; font-weight: 500; display: block; margin-top: 1px; }

  .hero { position: absolute; top: 71px; left: 0; width: 1200px; height: 600px; display: block; }

  .intro { position: absolute; top: 606px; left: 0; width: 1200px; text-align: center; }
  .section-title { font-family: var(--head-font); font-weight: 700; font-size: 46px; color: var(--ink); letter-spacing: -1px; }
  .section-title span { color: var(--green); }
  .intro p { width: 680px; margin: 16px auto 0; font-size: 15px; line-height: 24px; color: var(--text); }

  .service { position: absolute; left: 0; width: 1200px; }
  .service--grey { background: var(--grey-band); }
  .service-photo { position: absolute; width: 354px; height: 354px; border-radius: 50%; background: var(--green); }
  .service-photo::before { content: ""; position: absolute; inset: 20px; border-radius: 50%; background: var(--white); }
  .service-photo .photo-fill { position: absolute; inset: 26px; border-radius: 50%; }
  .service-copy { position: absolute; width: 400px; }
  .service-name { font-family: var(--head-font); font-weight: 700; font-size: 40px; color: var(--ink); letter-spacing: -0.5px; margin-bottom: 26px; }
  .ticks { list-style: none; }
  .ticks li { position: relative; padding-left: 28px; font-size: 15px; line-height: 24px; margin-bottom: 23px; }
  .ticks svg { position: absolute; left: 0; top: 5px; }

  .cta { position: absolute; top: 2290px; left: 0; width: 1200px; height: 397px; }
  .cta-art { position: absolute; inset: 0; display: block; }
  .cta-heading { position: absolute; top: 174px; width: 1200px; text-align: center; font-family: var(--head-font); font-weight: 900; font-size: 31px; line-height: 42px; color: var(--white); letter-spacing: -1px; }
  .cta-button { position: absolute; left: 479px; top: 268px; width: 242px; height: 47px; background: var(--ink); color: var(--white); border-radius: 4px; display: flex; align-items: center; justify-content: center; gap: 12px; font-family: var(--head-font); font-weight: 500; font-size: 17px; text-decoration: none; }

  .site-footer { position: absolute; top: 2687px; left: 0; width: 1200px; height: 354px; background: var(--charcoal); color: var(--white); }
  .site-footer .brand { left: 132px; top: 88px; }
  .site-footer .brand-main { font-size: 56px; }
  .site-footer .brand-sub { font-size: 13px; letter-spacing: 1px; margin: 3px 0 0 86px; }
  .footer-col { position: absolute; top: 72px; list-style: none; font-family: var(--head-font); }
  .footer-col li { font-size: 15px; font-weight: 500; height: 35px; }
  .footer-col .col-title { font-weight: 500; font-size: 15px; height: 34px; }
  .footer-col .sub-link { font-family: var(--body-font); font-weight: 400; font-size: 13px; height: 27px; text-decoration: underline; }
  .footer-map { position: absolute; left: 786px; top: 73px; width: 282px; height: 110px; background: linear-gradient(135deg, #e4ecd9, #d7e3ee 60%, #e9e6d6); border-bottom: 3px solid #f0b44a; }
  .social { position: absolute; top: 232px; left: 0; width: 1200px; display: flex; justify-content: center; gap: 6px; }
  .social a { width: 33px; height: 33px; border: 1.5px solid #cfcfcf; border-radius: 50%; display: block; }
  .footer-rule { position: absolute; top: 287px; left: 27px; width: 1146px; border-top: 1px solid #555; }
  .copyright { position: absolute; top: 308px; width: 1200px; text-align: center; font-size: 14px; color: #d5d5d5; }
</style>
</head>
<body>

<header class="site-header">
  <a class="brand" href="#"><span class="brand-main">BRINDLE</span><span class="brand-sub">LANDSCAPES</span></a>
  <nav class="main-nav">
    <a href="#">HOME</a>
    <a href="#">SERVICES</a>
    <a href="#" class="is-current">ABOUT</a>
    <a href="#">OUR WORK</a>
    <a href="#">CONTACT</a>
  </nav>
  <div class="estimate-box">
    <span class="estimate-label">FREE ESTIMATES</span>
    <span class="estimate-phone">07700 900417</span>
  </div>
</header>

<svg class="hero" viewBox="0 0 1200 600" width="1200" height="600">
  <defs>
    <linearGradient id="heroPhoto" x1="0" y1="0" x2="1" y2="1">
      <stop offset="0" stop-color="#8a6a4a"/>
      <stop offset="0.35" stop-color="#6fa23a"/>
      <stop offset="0.7" stop-color="#5b8f2e"/>
      <stop offset="1" stop-color="#4b3c30"/>
    </linearGradient>
  </defs>
  <rect width="1200" height="600" fill="url(#heroPhoto)" role="img" aria-label="Garden with artificial lawn, timber sleeper steps and rattan patio furniture"/>
  <path d="M0,584 Q560,300 1200,418 L1200,600 L0,600 Z" fill="#ffffff"/>
  <path d="M0,558 Q520,248 1200,408 L1200,418 Q560,300 0,584 Z" fill="#5cb82e"/>
</svg>

<section class="intro">
  <h1 class="section-title">OUR <span>SERVICES</span></h1>
  <p>Brindle landscapes offer a comprehensive range of landscaping services. They include paving and brickwork, fencing, decking, pergolas, artificial grass, driveways, and turfing and planting. We work with garden designers but working closely with our customers we feel they aren't always necessary to achieve an outstanding finished project.</p>
</section>

<section class="service service--grey" style="top:859px;height:471px;">
  <div class="service-photo" style="left:212px;top:57px;">
    <div class="photo-fill" role="img" aria-label="Newly laid block paved driveway" style="background:linear-gradient(160deg,#6f7d5c,#9d9180 45%,#7d7a78);"></div>
  </div>
  <div class="service-copy" style="left:645px;top:128px;">
    <h2 class="service-name">DRIVEWAYS</h2>
    <ul class="ticks">
      <li><svg width="16" height="12" viewBox="0 0 16 12"><polyline points="1,6 6,10.5 15,1" fill="none" stroke="#5cb82e" stroke-width="2.4"/></svg>We cater for every budget. You can increase the value of your home with a relatively small investment.</li>
      <li><svg width="16" height="12" viewBox="0 0 16 12"><polyline points="1,6 6,10.5 15,1" fill="none" stroke="#5cb82e" stroke-width="2.4"/></svg>All our driveways are built to last!</li>
    </ul>
  </div>
</section>

<section class="service" style="top:1330px;height:490px;">
  <div class="service-copy" style="left:185px;top:135px;">
    <h2 class="service-name">PAVING</h2>
    <ul class="ticks">
      <li><svg width="16" height="12" viewBox="0 0 16 12"><polyline points="1,6 6,10.5 15,1" fill="none" stroke="#5cb82e" stroke-width="2.4"/></svg>We have a vast knowledge of paving materials, helping you make the right choices.</li>
      <li><svg width="16" height="12" viewBox="0 0 16 12"><polyline points="1,6 6,10.5 15,1" fill="none" stroke="#5cb82e" stroke-width="2.4"/></svg>We can help you transform your garden giving you a functional and attractive space.</li>
    </ul>
  </div>
  <div class="service-photo" style="left:634px;top:62px;">
    <div class="photo-fill" role="img" aria-label="Grey slab patio beside a lawn and brick wall" style="background:linear-gradient(160deg,#8a5a44,#5c9a32 35%,#b9bcc0 60%,#9fa3a8);"></div>
  </div>
</section>

<section class="service service--grey" style="top:1820px;height:470px;">
  <div class="service-photo" style="left:212px;top:56px;">
    <div class="photo-fill" role="img" aria-label="New timber closeboard fence with bark border and stone path" style="background:linear-gradient(170deg,#9b6a55,#c9a76c 40%,#a8855a 65%,#6b4a35);"></div>
  </div>
  <div class="service-copy" style="left:645px;top:123px;">
    <h2 class="service-name">FENCING</h2>
    <ul class="ticks">
      <li><svg width="16" height="12" viewBox="0 0 16 12"><polyline points="1,6 6,10.5 15,1" fill="none" stroke="#5cb82e" stroke-width="2.4"/></svg>We offer all aspects of fencing, installed to an extremely high standard.</li>
      <li><svg width="16" height="12" viewBox="0 0 16 12"><polyline points="1,6 6,10.5 15,1" fill="none" stroke="#5cb82e" stroke-width="2.4"/></svg>From the smallest post to the largest fence, we provide a prompt and friendly fencing service you can depend on.</li>
    </ul>
  </div>
</section>

<section class="cta">
  <svg class="cta-art" viewBox="0 0 1200 397" width="1200" height="397">
    <defs>
      <linearGradient id="ctaPhoto" x1="0" y1="0" x2="1" y2="1">
        <stop offset="0" stop-color="#4e9a2a"/>
        <stop offset="0.5" stop-color="#7cc25a"/>
        <stop offset="1" stop-color="#4a8f27"/>
      </linearGradient>
    </defs>
    <rect width="1200" height="397" fill="#ebebeb"/>
    <path d="M0,226 Q560,-30 1200,62 L1200,397 L0,397 Z" fill="url(#ctaPhoto)" role="img" aria-label="Paved patio with timber pergola under a green tint"/>
    <path d="M0,206 Q540,-58 1200,46 L1200,62 Q560,-30 0,226 Z" fill="#5cb82e"/>
  </svg>
  <h2 class="cta-heading">YOUR GARDEN AND DRIVEWAY CARED FOR<br>THE WAY THEY SHOULD BE</h2>
  <a class="cta-button" href="#">START MY ESTIMATE
    <svg width="17" height="17" viewBox="0 0 17 17"><circle cx="8.5" cy="8.5" r="8.5" fill="#ffffff"/><polyline points="7,5 10.5,8.5 7,12" fill="none" stroke="#231f20" stroke-width="2"/></svg>
  </a>
</section>

<footer class="site-footer">
  <a class="brand" href="#"><span class="brand-main">BRINDLE</span><span class="brand-sub">LANDSCAPES</span></a>
  <ul class="footer-col" style="left:385px;top:76px;">
    <li>HOME</li><li>ABOUT US</li><li>OUR WORK</li><li>CONTACT</li>
  </ul>
  <ul class="footer-col" style="left:505px;">
    <li class="col-title">SERVICES</li>
    <li class="sub-link">Driveways</li><li class="sub-link">Paving</li><li class="sub-link">Fencing</li>
  </ul>
  <ul class="footer-col" style="left:633px;">
    <li class="col-title">QUICK LINKS</li>
    <li class="sub-link">FAQ</li><li class="sub-link">Testimonials</li><li class="sub-link">Sitemap</li>
  </ul>
  <div class="footer-map" role="img" aria-label="Map showing the company location"></div>
  <div class="social">
    <a href="#" aria-label="Social profile one"></a>
    <a href="#" aria-label="Social profile two"></a>
    <a href="#" aria-label="Social profile three"></a>
    <a href="#" aria-label="Social profile four"></a>
  </div>
  <div class="footer-rule"></div>
  <p class="copyright">© 2020 Brindle Landscapes. All Rights are Reserved.</p>
</footer>

</body>
</html>
```